K.T.W Services

We are needing business cards for a construction company that does everything from painting and detailing, maintenance, Sheetrock repairs, demolition, tile and wood floors. Also, K.T.W stands for Detailing, maintenance, and Painting. We would like the colors to be closer to the colors grey and light brown/khaki, but if there is any other suggestions that would go better with the design we are open to ideas.

Industry/Entity Type

Business

Contact Information for Business Card

Owner / Operator Owen Haskell (555) 314-2097 / (555) 482- 3916

Font styles to use
Sans Serif

```html
<!DOCTYPE html>
<html lang="en">
<head>
<meta charset="utf-8">
<title>K.T.W Services – Business Cards</title>
<link rel="stylesheet" href="https://fonts.googleapis.com/css2?family=Source+Sans+3:wght@400;600;700&display=swap">
<style>
  :root {
    --backdrop: #2f2925;
    --card: #1b1b1b;
    --card-edge: #262626;
    --gold: #c9a13a;
    --white: #f2f2f2;
  }
  * { margin: 0; padding: 0; box-sizing: border-box; }
  html, body {
    width: 1200px; height: 844px; overflow: hidden;
    background: var(--backdrop);
    font-family: "Source Sans 3", "Helvetica Neue", Arial, sans-serif;
  }
  .stage {
    width: 1200px; height: 844px;
    display: flex; align-items: center; justify-content: center; gap: 40px;
  }
  .card {
    position: relative;
    width: 520px; height: 297px;
    background: var(--card);
    border: 1px solid var(--card-edge);
    box-shadow: 0 10px 30px rgba(0,0,0,.45);
    color: var(--white);
  }
  .brand-name {
    position: absolute;
    font-weight: 700; color: var(--gold);
    letter-spacing: 2px; line-height: 1; white-space: nowrap;
  }
  /* Front */
  .card-front .brand-name { left: 168px; top: 78px; font-size: 64px; }
  .contact-person {
    position: absolute; left: 224px; top: 212px; text-align: center;
  }
  .person-name { color: var(--gold); font-weight: 700; font-size: 18px; line-height: 22px; }
  .person-role { color: var(--white); font-size: 15px; line-height: 20px; }
  .contact-phones {
    position: absolute; left: 378px; top: 178px;
    list-style: none; font-size: 15px;
  }
  .contact-phones li { display: flex; align-items: center; gap: 6px; line-height: 21px; white-space: nowrap; }
  .phone-icon { width: 10px; height: 10px; fill: var(--gold); flex: none; }
  /* Back */
  .card-back .brand-name { left: 50%; top: 46px; transform: translateX(-50%); font-size: 50px; }
  .divider {
    position: absolute; left: 0; right: 0; top: 140px;
    height: 1px; background: linear-gradient(90deg, transparent, var(--gold) 30%, var(--gold) 70%, transparent);
  }
  .services {
    position: absolute; left: 0; right: 0; top: 128px; text-align: center;
  }
  .services-title {
    display: inline-block; padding: 0 10px; background: var(--card);
    color: var(--gold); font-weight: 600; font-size: 18px; line-height: 24px; position: relative;
  }
  .services-list { list-style: none; margin-top: 6px; font-size: 14px; line-height: 18px; font-weight: 600; }
</style>
</head>
<body>
<main class="stage">
  <section class="card card-front" aria-label="Business card front">
    <span class="brand-name">K.T.W</span>
    <div class="contact-person">
      <p class="person-name">Owen Haskell</p>
      <p class="person-role">Owner / Operator</p>
    </div>
    <ul class="contact-phones">
      <li><svg class="phone-icon" viewBox="0 0 24 24" aria-hidden="true"><path d="M6.6 10.8a15 15 0 0 0 6.6 6.6l2.2-2.2a1 1 0 0 1 1-.25 11.4 11.4 0 0 0 3.6.6 1 1 0 0 1 1 1V20a1 1 0 0 1-1 1A17 17 0 0 1 3 4a1 1 0 0 1 1-1h3.5a1 1 0 0 1 1 1 11.4 11.4 0 0 0 .6 3.6 1 1 0 0 1-.25 1z"/></svg>(555) 314-2097</li>
      <li><svg class="phone-icon" viewBox="0 0 24 24" aria-hidden="true"><path d="M6.6 10.8a15 15 0 0 0 6.6 6.6l2.2-2.2a1 1 0 0 1 1-.25 11.4 11.4 0 0 0 3.6.6 1 1 0 0 1 1 1V20a1 1 0 0 1-1 1A17 17 0 0 1 3 4a1 1 0 0 1 1-1h3.5a1 1 0 0 1 1 1 11.4 11.4 0 0 0 .6 3.6 1 1 0 0 1-.25 1z"/></svg>(555) 482- 3916</li>
    </ul>
  </section>

  <section class="card card-back" aria-label="Business card back">
    <span class="brand-name">K.T.W</span>
    <div class="divider"></div>
    <div class="services">
      <h2 class="services-title">Our Services</h2>
      <ul class="services-list">
        <li>Painting and Detailing</li>
        <li>Maintenance</li>
        <li>Sheetrock Repairs</li>
        <li>Demolition</li>
        <li>Tile and Wood Floors</li>
      </ul>
    </div>
  </section>
</main>
</body>
</html>
```